Vintage soap dispenser label

I'm making a series of glass bottle soap dispensers (soap, lotion, shampoo, etc.). I really love a competitor's design, but I don't want to copy it. I'm interested in the clean, urban vintage style. There can be a lot of filler text as in their design which fills the negative space, but note that the buyer will fill the bottles with their own products, so things like "100% Natural Ingredients" and the like are somewhat bogus. Because they are to be refillable, reusable bottles, some text to that effect may be more appropriate, plus our company name "Velmora Home", and perhaps the style of the bottle "Boston Round" and other text like the size of the bottle. I need a basic design, 3.25" wide x 3.5" tall and I will adjust the text as necessary for the various products my buyers will use. My competitor that is very similar to my business is https://qorvu.ly/8LmZr5k. As you can see, they have a signature style. I'd like my own signature style. (I plan to have a vintage line and a contemporary line of products, so I'll likely be posting a second request for that.)

Requirements
Should not have
• Not too ornate. Should be somewhat minimalistic

```html
<!DOCTYPE html>
<html lang="en">
<head>
<meta charset="UTF-8">
<title>Velmora Home – Boston Round Label</title>
<link rel="stylesheet" href="https://fonts.googleapis.com/css2?family=Alfa+Slab+One&family=Source+Sans+3:wght@400&display=swap">
<style>
  :root {
    --ink: #231f20;
    --paper: #ffffff;
  }
  html, body {
    margin: 0;
    padding: 0;
    width: 1200px;
    height: 1200px;
    overflow: hidden;
    background: var(--paper);
  }
  .label {
    display: block;
    width: 1200px;
    height: 1200px;
  }
  .rule { stroke: var(--ink); fill: none; }
  .rule--solid { stroke-width: 2.5; }
  .rule--dashed { stroke-width: 1.6; stroke-dasharray: 4 3; }
  .display {
    font-family: "Alfa Slab One", serif;
    fill: var(--ink);
  }
  .caption {
    font-family: "Source Sans 3", sans-serif;
    fill: var(--ink);
  }
</style>
</head>
<body>
<svg class="label" viewBox="0 0 1200 1200" xmlns="http://www.w3.org/2000/svg" aria-label="Velmora Home bottle label">
  <!-- outer frame -->
  <circle class="rule rule--solid" cx="600" cy="600" r="558"/>
  <circle class="rule rule--dashed" cx="600" cy="600" r="543"/>

  <!-- volume badge -->
  <g class="volume-badge">
    <circle class="rule rule--solid" cx="600" cy="278" r="140"/>
    <circle class="rule rule--dashed" cx="600" cy="278" r="129"/>
    <line class="rule rule--dashed" x1="474" y1="271" x2="726" y2="271"/>
    <text class="display" x="600" y="257" font-size="62" text-anchor="middle">300ML</text>
    <text class="caption" x="600" y="318" font-size="29" text-anchor="middle">10.14 FL OZ</text>
  </g>

  <!-- brand name -->
  <text class="display brand-name" x="600" y="586" font-size="150" text-anchor="middle" textLength="960" lengthAdjust="spacingAndGlyphs">VELMORA HOME</text>

  <!-- feature band -->
  <line class="rule rule--solid" x1="41" y1="624" x2="1159" y2="624"/>
  <line class="rule rule--solid" x1="71" y1="785" x2="1129" y2="785"/>
  <line class="rule rule--solid" x1="600" y1="642" x2="600" y2="768"/>
  <text class="caption" x="553" y="730" font-size="67" text-anchor="end">REFILLABLE</text>
  <text class="caption" x="641" y="730" font-size="67" text-anchor="start">REUSABLE</text>

  <!-- bottle style band -->
  <line class="rule rule--dashed" x1="104" y1="821" x2="1096" y2="821"/>
  <line class="rule rule--dashed" x1="161" y1="919" x2="1039" y2="919"/>
  <text class="caption" x="600" y="887" font-size="48" text-anchor="middle">BOSTON ROUND</text>

  <!-- number badge -->
  <g class="number-badge">
    <circle class="rule rule--solid" cx="600" cy="1044" r="94"/>
    <circle class="rule rule--dashed" cx="600" cy="1044" r="84"/>
    <text class="display" x="600" y="1062" font-size="44" text-anchor="middle">NO. 01</text>
  </g>
</svg>
</body>
</html>
```